Fundraising Brochure Design for Environmental Organization

We need a fundraising brochure designed for the Gable and Marsh Streamwarden. This is an environmental group that helps keep the Gable and Marsh rivers open to the public and clean for swimming and fishing. The brochure will be used to help raise money for the organization. The brochure text, layout and image options, are given. Also included are two examples of brochures we like. The layout should be clean (not cluttered), easy to read, and attractive to look at. It should communicate the beauty of the rivers and encourage people to get involved.
Updates

Hello Everyone, Thank you for submitting so many wonderful designs!! We are working with our client to review each one. Next week we will contact you with feedback from the client, and let you know if they have any requests for changes to the designs before making the final decision. Have a great weekend!

Hello Designers, Thank you for submitting such wonderful designs. We will be meeting soon to discuss the designs with our client. Once we get feedback from them we will be in touch. Thank you for your patience.

Target Market(s)

The target audience for this brochure includes people who are rich homeowners, over 60 years old, who may have a vacation home, have a high-paying job, may own their own business, may be a doctor, lawyer, etc., dive a luxury car, and owns a boat or airplane.

The target audience also includes people who travel a lot, may be retired, even at a young age, and also younger people who are wealthy through inheritance.

Industry/Entity Type

Group

Requirements
Must have
• Must be a tri-fold brochure matching the dimensions provided in the Brochure Interior and Exterior Dimensions files.
Each page must include the text provided in the Fundraising Brochure Text file.
The logos listed in the Fundraising Brochure Text file are provided and must be included in the brochure where indicated.
Should not have
• There should be no pictures of pools.
Not all of the photos provided should be used in the brochure.
Do not edit the text.

```html
<!DOCTYPE html>
<html lang="en">
<head>
<meta charset="utf-8">
<title>Gable and Marsh Streamwarden – Fundraising Tri-fold</title>
<link href="https://fonts.googleapis.com/css2?family=Source+Sans+3:wght@400;600;700&display=swap" rel="stylesheet">
<style>
  :root{
    --stage:#2f6fc4;
    --navy:#1f3a7a;
    --deep:#0f3f86;
    --water:#1f64b4;
    --water-light:#3c8fd6;
    --sky:#9cd0f2;
    --paper:#e9eef5;
    --paper-blue:#cfe0f1;
    --ink:#1d2433;
    --white:#ffffff;
    --money:#8aa07a;
    --map-land:#d8b79a;
    --map-water:#6b8fc9;
  }
  *{box-sizing:border-box;margin:0;padding:0}
  html,body{width:1200px;height:1000px;overflow:hidden}
  body{background:var(--stage);font-family:"Source Sans 3",Arial,sans-serif;color:var(--ink);position:relative}
  .spread{position:absolute;left:20px;width:1160px;height:470px;display:grid;grid-template-columns:repeat(3,1fr);box-shadow:0 6px 18px rgba(0,0,0,.25)}
  .spread--inside{top:18px;background:linear-gradient(180deg,var(--water-light) 25%,var(--water) 60%,var(--deep) 100%)}
  .spread--outside{top:510px}
  .panel{position:relative;overflow:hidden;border-right:1px solid rgba(255,255,255,.25)}
  .panel:last-child{border-right:0}

  /* inside */
  .shore-photo{position:absolute;top:0;left:0;right:0;height:130px;background:linear-gradient(180deg,#cfe8f7 0%,#7fb35a 35%,#3f7a2a 65%,#2e74b8 100%)}
  .inside-text{position:absolute;top:150px;left:22px;right:22px;color:var(--white);font-size:10.5px;line-height:1.38}
  .inside-text h2{font-size:17px;font-weight:700;margin-bottom:8px}
  .inside-text p{margin-bottom:8px}
  .inside-text ul{list-style:none}
  .inside-text li{padding-left:10px;position:relative;margin-bottom:3px}
  .inside-text li::before{content:"–";position:absolute;left:0}
  .reef-photo{position:absolute;right:0;bottom:0;width:100%;height:150px;background:linear-gradient(180deg,rgba(15,63,134,0) 0%,rgba(40,90,120,.6) 100%)}

  /* outside */
  .panel--help{background:linear-gradient(180deg,var(--paper) 0%,var(--paper-blue) 55%,var(--water-light) 100%);padding:20px 22px;font-size:10px;line-height:1.35}
  .panel--help h2{font-size:18px;font-weight:600;color:var(--ink);margin-bottom:8px}
  .panel--help p{margin-bottom:7px;max-width:300px}
  .panel--help strong{font-weight:700}
  .bill-photo{position:absolute;top:10px;right:20px;width:70px;height:40px;background:linear-gradient(135deg,#c9d4bd,var(--money))}
  .hand-photo{position:absolute;bottom:16px;right:22px;width:150px;height:54px;background:linear-gradient(90deg,var(--money),#e6c2a4 70%,var(--ink) 100%)}

  .panel--reply{background:var(--paper);padding:16px 20px;font-size:9.5px;line-height:1.3}
  .address{margin-bottom:8px}
  .badges{display:flex;gap:10px;margin-bottom:8px}
  .badge{width:60px;height:18px;background:var(--paper-blue);border-radius:3px}
  .badge--round{width:18px;border-radius:50%}
  .map{width:150px;height:90px;margin:0 auto 10px;background:linear-gradient(135deg,var(--map-land) 55%,var(--map-water) 100%)}
  .form{border:1.5px dashed var(--ink);padding:8px 10px;font-size:8.5px}
  .form-row{display:grid;grid-template-columns:1fr 1fr;gap:4px 12px}
  .field{display:flex;align-items:center;gap:4px;margin-bottom:3px}
  .field span{width:32px;white-space:nowrap}
  .field span.wide{width:auto}
  .field i{flex:1;height:11px;border:1px solid var(--ink);background:var(--white)}
  .check{display:flex;align-items:center;gap:4px;margin-bottom:2px;white-space:nowrap}
  .check i{width:8px;height:8px;border:1px solid var(--ink);background:var(--white)}
  .form h4{font-size:9px;margin:4px 0 3px}
  .pay{display:flex;gap:12px;align-items:center;margin-bottom:3px}
  .signature{margin-top:8px;font-size:9px}
  .signature h4{font-size:11px}

  .panel--cover{background:linear-gradient(180deg,var(--sky) 0%,#dbeaf6 35%,var(--paper) 55%)}
  .brand{position:absolute;top:95px;left:0;right:0;text-align:center}
  .brand-mark{display:inline-flex;align-items:center;gap:8px;color:var(--navy);font-weight:700;font-size:24px;line-height:1.05}
  .brand-mark i{width:26px;height:26px;border-radius:50%;background:var(--navy);flex:none}
  .tagline{margin-top:10px;color:var(--water);font-size:13px;line-height:1.3}
  .cover-photo{position:absolute;left:0;right:0;bottom:0;height:190px;background:linear-gradient(180deg,#dfeaf3 0%,#5f9a3d 25%,#2f6a22 50%,var(--water) 70%,var(--deep) 100%)}
</style>
</head>
<body>

<section class="spread spread--inside" aria-label="Brochure inside">
  <article class="panel">
    <div class="shore-photo" role="img" aria-label="Wooded river shoreline with gulls in flight"></div>
    <div class="inside-text">
      <h2>Beautiful Rivers in Peril</h2>
      <p>You love these rivers – that's why you're here. And you're troubled by the signs that show these waters are threatened by pollution, erosion and a changing climate. Crumbling shorelines, disappearing islands, water so clogged with silt and clouded with algae that no underwater grasses can grow to provide habitat for fish and crabs, and oysters are struggling to survive. The rivers teem with bacteria after every rain.</p>
      <p>These rivers need help, and that's why there's a Streamwarden. We share your passion – and your concern. For the past decade, we've been the only citizen environmental organization solely dedicated to protecting and restoring the Gable and Marsh Rivers, one creek at a time.</p>
    </div>
  </article>
  <article class="panel">
    <div class="shore-photo" role="img" aria-label="Sailboat on the river in front of a tree line"></div>
    <div class="inside-text">
      <h2>How we work to protect our rivers</h2>
      <p>We work to make these rivers safe for swimming, fishing and wildlife by "keeping" your watershed with grants from public and private sources to:</p>
      <ul>
        <li>Advocate for better environmental policies</li>
        <li>Enforce environmental laws</li>
        <li>Monitor water quality</li>
        <li>Expand public access to the water</li>
        <li>Promote pump-out service to recreational boaters</li>
        <li>Create and restore new forest buffers, wetlands and living shorelines that naturally filter stormwater and stop pollution</li>
      </ul>
    </div>
  </article>
  <article class="panel">
    <div class="shore-photo" role="img" aria-label="River shoreline with a hot-air balloon in the sky"></div>
    <div class="inside-text">
      <h2>Who we are</h2>
      <p>The Streamwarden serves as a voice for the rivers, working with local community groups, regional and national partners, and county, state and federal officials to enforce laws, advocate policies and engage citizens through education, monitoring and hands-on restoration of our shared waters.</p>
    </div>
    <div class="reef-photo" role="img" aria-label="Underwater scene with tropical fish and coral"></div>
  </article>
</section>

<section class="spread spread--outside" aria-label="Brochure outside">
  <article class="panel panel--help">
    <div class="bill-photo" role="img" aria-label="Floating dollar bill"></div>
    <h2>How can you help?</h2>
    <p>Just as the rivers need the Streamwarden, the Streamwarden needs your help. Your financial gift is vital to the success of our efforts.</p>
    <p><strong>We will leverage your tax-deductible contribution up to four times its value in grants</strong> from corporations, private foundations, as well as county, state and federal resources.</p>
    <p><strong>Every dollar you give means we can do $5 worth of work</strong> – planting trees, growing oysters, restoring marshes and streambeds, creating wetlands, and living shorelines that protect the Gable and Marsh Rivers for generations to come.</p>
    <p><strong>There's a lot to do, and we couldn't do all we do without you.</strong> Join us as a volunteer, become a member, or consider making a meaningful financial contribution to help us protect these rivers that we all love.</p>
    <p>How? Log on to www.gablemarshwarden.org, or call 555-014-2290. Or fill out the attached form and send it in with a check made out to Gable and Marsh Streamwarden, Inc.</p>
    <div class="hand-photo" role="img" aria-label="Hand holding out dollar bills"></div>
  </article>

  <article class="panel panel--reply">
    <div class="address">
      Gable and Marsh Streamwarden, Inc.<br>
      112 Heron Point Lane<br>
      Millbrook Cove, ST 00412<br>
      555-014-2290<br>
      warden@gablemarshwarden.org<br>
      www.gablemarshwarden.org
    </div>
    <div class="badges" aria-label="Partner organizations">
      <span class="badge"></span><span class="badge badge--round"></span><span class="badge"></span>
    </div>
    <div class="map" role="img" aria-label="Map of the Gable and Marsh river watershed"></div>
    <div class="form">
      <div class="form-row">
        <div>
          <div class="field"><span>Name</span><i></i></div>
          <div class="field"><span>Street</span><i></i></div>
          <div class="field"><span>State</span><i></i></div>
          <div class="field"><span>Email</span><i></i></div>
        </div>
        <div>
          <div class="field"><span>City</span><i></i></div>
          <div class="field"><span>Zip</span><i></i></div>
          <div class="field"><span>Phone</span><i></i></div>
        </div>
        <div>
          <div class="check"><i></i>Individual $35</div>
          <div class="check"><i></i>Supporter $100</div>
          <div class="check"><i></i>Steward $250</div>
          <div class="check"><i></i>Legacy $1000</div>
        </div>
        <div>
          <div class="check"><i></i>Family $50</div>
          <div class="check"><i></i>Patron $500</div>
          <div class="check"><i></i>Visionary $5000</div>
        </div>
      </div>
      <h4>Payment Method</h4>
      <div class="pay"><span class="check"><i></i>Check</span><span class="check"><i></i>Credit Card</span><span class="check"><i></i>Debit Card</span></div>
      <div class="form-row">
        <div class="field"><span class="wide">Security Code</span><i></i></div>
        <div class="field"><span class="wide">Exp. Date</span><i></i></div>
      </div>
    </div>
    <div class="signature">
      <h4>Signature</h4>
      Gable and Marsh Streamwarden, Inc. is a 501 (c) 3 nonprofit organization, and all contributions are tax deductible.
    </div>
  </article>

  <article class="panel panel--cover">
    <div class="brand">
      <div class="brand-mark"><i></i><span>Gable and Marsh<br>Streamwarden</span></div>
      <p class="tagline">Protecting the Gable and Marsh Rivers<br>for generations to come.</p>
    </div>
    <div class="cover-photo" role="img" aria-label="Tree-lined riverbank reflected in calm blue water"></div>
  </article>
</section>

</body>
</html>
```